Our architectural studio needs a new business card

We need a business card design for our studio based in Valmorée in Belgium. We are active in architecture, design and installation.
Our works are contemporary and minimalist. our clients are refined and cultured.
Our business card must be minimalist and refined.

Reason: Some designers have accepted my invitation but they don't have all replied. I want to give them a chance to make one proposal. Paul

Target Market(s)

architecture

Industry/Entity Type

Business

Contact Information for Business Card

studio: paul dorsande studio
paul dorsande, architecte
M. +32 471 982 615
F. +322 618 4097
www.pauldorsande-example.com
paul@pauldorsande-example.com
14 rue des Margelles
1395 Valmorée
Belgium

Font styles to use
Sans Serif

Requirements
Must have
• simple, minimalist, clear, elegant and chic! Black and white
Nice to have
• embossed logo, other format like a square for example
Should not have
• color, fantasy, curves, ...

```html
<!DOCTYPE html>
<html lang="fr">
<head>
<meta charset="utf-8">
<title>Paul Dorsande Studio — Business Card</title>
<link href="https://fonts.googleapis.com/css2?family=Fira+Sans:wght@400;500;600&display=swap" rel="stylesheet">
<style>
  :root {
    --backdrop: #e7e7e7;
    --paper: #f7f7f5;
    --ink: #1b1b1b;
    --card-black: #161616;
    --deboss: #2c2c2c;
  }
  * { margin: 0; padding: 0; box-sizing: border-box; }
  html, body { width: 1200px; height: 720px; overflow: hidden; }
  body {
    background: var(--backdrop);
    font-family: "Fira Sans", Arial, sans-serif;
    position: relative;
  }
  .card {
    position: absolute;
    top: 242px;
    width: 420px;
    height: 239px;
    overflow: hidden;
  }
  .card--front { left: 147px; background: var(--paper); color: var(--ink); }
  .card--back { left: 633px; background: var(--card-black); }

  /* front */
  .front__mark {
    position: absolute;
    left: 64px; top: 64px;
    width: 130px; height: 110px;
    display: flex; flex-direction: column; align-items: flex-end; justify-content: flex-end;
    gap: 8px;
  }
  .front__mark-square { width: 16px; height: 16px; background: var(--ink); }
  .front__mark-name {
    font-weight: 600; font-size: 17px; line-height: 1.1; text-align: right; color: var(--ink);
  }
  .front__divider {
    position: absolute; left: 210px; top: 36px;
    width: 2px; height: 174px; background: var(--ink);
  }
  .front__details { position: absolute; left: 242px; top: 55px; width: 170px; }
  .front__name { font-weight: 600; font-size: 13px; line-height: 15px; }
  .front__role { font-size: 10px; line-height: 12px; font-weight: 500; }
  .front__address { margin-top: 14px; font-size: 10px; line-height: 13px; font-weight: 500; }
  .front__contacts { margin-top: 13px; list-style: none; font-size: 9.5px; line-height: 13px; font-weight: 500; }
  .front__contacts li { display: flex; align-items: center; gap: 7px; white-space: nowrap; }
  .front__contacts svg { width: 10px; height: 9px; fill: var(--ink); flex: none; }
  .front__rule {
    position: absolute; left: 0; right: 0; bottom: 22px; height: 1.5px; background: var(--ink);
  }
  .front__band {
    position: absolute; left: 0; right: 0; bottom: 0; height: 19px; background: var(--ink);
  }

  /* back */
  .back__mark {
    position: absolute; left: 0; right: 0; top: 58px;
    display: flex; flex-direction: column; align-items: center; gap: 10px;
  }
  .back__mark-square { width: 22px; height: 22px; background: var(--deboss); }
  .back__mark-name { font-weight: 600; font-size: 24px; color: var(--deboss); }
  .back__studio {
    position: absolute; left: 0; right: 0; top: 196px;
    text-align: center; font-size: 10.5px; letter-spacing: 4.2px;
    text-transform: uppercase; color: var(--deboss); font-weight: 500;
  }
</style>
</head>
<body>
  <section class="card card--front">
    <div class="front__mark">
      <span class="front__mark-square"></span>
      <span class="front__mark-name">paul dorsande<br>studio</span>
    </div>
    <div class="front__divider"></div>
    <div class="front__details">
      <p class="front__name">Paul Dorsande</p>
      <p class="front__role">Architecte</p>
      <p class="front__address">14 rue des Margelles 1395<br>Valmorée Belgium</p>
      <ul class="front__contacts">
        <li><svg viewBox="0 0 10 9"><path d="M1 3.2C1 2 2.5 1 5 1s4 1 4 2.2V4H7V3H3v1H1z M2.5 4.5h5L8.5 8h-7z"/></svg>+32 471 982 615</li>
        <li><svg viewBox="0 0 10 9"><path d="M2.5 0h5v2.5h-5z M0 3h10v4H8V5.5H2V7H0z M2.5 6h5v3h-5z"/></svg>+322 618 4097</li>
        <li><svg viewBox="0 0 10 9"><path d="M0 1h10v7H0z"/><path d="M0.6 1.6L5 5l4.4-3.4" stroke="#f7f7f5" stroke-width="1" fill="none"/></svg>paul@pauldorsande-example.com</li>
        <li><svg viewBox="0 0 10 9"><path d="M0 0.5h10v6H0z M1 1.5v4h8v-4z M3 7.5h4V9H3z"/></svg>www.pauldorsande-example.com</li>
      </ul>
    </div>
    <div class="front__rule"></div>
    <div class="front__band"></div>
  </section>

  <section class="card card--back">
    <div class="back__mark">
      <span class="back__mark-square"></span>
      <span class="back__mark-name">paul dorsande studio</span>
    </div>
    <p class="back__studio">Paul Dorsande Studio</p>
  </section>
</body>
</html>
```